"Grandpa's Old Mule" Bookcover 170501

We need a book cover for print edition of the title, "Grandpa's Old Mule". The book is about the life of a man and that of his last dog, told from the perspective of his son. The book is a mix of highly improbable situations and a son's remembrance of his father. We've attached pictures of both the man and the dog, however, they do not have to be used, if it doesn't add to the design. It does provide an idea of what the subjects looked like. The author's name is Rob T. Venster. The publisher will be Quiet Heron Publishers. One book size template uploaded. NOTE: Designer credit will be included in the published work.

Target Market(s)

People who like non-fiction strange family and dog stories

Font styles to use
Serif
Sans Serif

Colors

Designer to choose colors to be used in the design.

Requirements
Must have
• A means of communicating a story about two lifetimes, the man and the dog. Full cover, front, spine and back.
Nice to have
• Man and Dog get equal billing, something that indicates a lifetime of events
Should not have
• A mere collage of the uploaded pics. Those can be used, but don't make it as simple as a photo album.

```html
<!DOCTYPE html>
<html lang="en">
<head>
<meta charset="utf-8">
<title>Grandpa's Old Mule — Full Cover</title>
<link href="https://fonts.googleapis.com/css2?family=Marcellus&display=swap" rel="stylesheet">
<style>
  :root {
    --ink: #141414;
    --ground: #000000;
    --paper-white: #ffffff;
    --title-yellow: #e9d83b;
    --title-orange: #f07436;
    --placeholder: #1b1b1b;
    --sky-top: #7276b3;
    --sky-mid: #b39190;
    --sky-gold: #ebb849;
    --sky-orange: #f29a3a;
    --sky-red: #e85a38;
  }
  * { margin: 0; padding: 0; box-sizing: border-box; }
  html, body { width: 1200px; height: 885px; overflow: hidden; background: var(--ground); }
  .cover {
    position: relative; width: 1200px; height: 885px; overflow: hidden;
    font-family: "Marcellus", serif;
  }
  .cover-scene { position: absolute; inset: 0; }

  .back-title {
    position: absolute; left: 20px; width: 548px; top: 38px;
    text-align: center; color: var(--ink); line-height: 0.95; font-weight: 400;
  }
  .back-title .line-one { display: block; font-size: 66px; }
  .back-title .line-two { display: block; font-size: 88px; }

  .back-blurb {
    position: absolute; left: 38px; width: 508px; top: 208px;
    font-size: 14.6px; line-height: 18.6px; color: var(--ink);
    text-align: center;
  }
  .author-photo {
    position: absolute; left: 35px; top: 533px; width: 187px; height: 230px;
    background: var(--placeholder);
  }
  .back-bio {
    position: absolute; left: 243px; width: 300px; top: 529px;
    font-size: 14.2px; line-height: 18.4px; color: var(--paper-white);
    text-align: left;
  }

  .spine-title, .spine-author {
    position: absolute; writing-mode: vertical-rl; transform: rotate(180deg);
    white-space: nowrap; left: 574px; width: 52px;
    display: flex; align-items: center; justify-content: center;
  }
  .spine-title { top: 40px; height: 400px; font-size: 36px; color: var(--ink); }
  .spine-author { top: 556px; height: 286px; font-size: 35px; color: var(--paper-white); }

  .front-author {
    position: absolute; right: 92px; top: 38px;
    font-size: 52px; color: var(--paper-white); letter-spacing: 1px;
  }
  .front-title { position: absolute; left: 0; top: 0; width: 1200px; height: 885px; font-weight: 400; }
  .front-title span { position: absolute; left: 708px; display: block; line-height: 1; white-space: nowrap; }
  .front-title .word-grandpa { top: 470px; font-size: 80px; color: var(--paper-white); }
  .front-title .word-old { top: 566px; font-size: 175px; color: var(--title-yellow); }
  .front-title .word-mule { top: 712px; font-size: 150px; color: var(--title-orange); }
</style>
</head>
<body>
<main class="cover">
  <svg class="cover-scene" width="1200" height="885" viewBox="0 0 1200 885">
    <defs>
      <linearGradient id="sky" x1="0" y1="0" x2="0" y2="1">
        <stop offset="0" stop-color="#7276b3"/>
        <stop offset="0.3" stop-color="#b39190"/>
        <stop offset="0.68" stop-color="#ebb849"/>
        <stop offset="0.86" stop-color="#f29a3a"/>
        <stop offset="1" stop-color="#e85a38"/>
      </linearGradient>
      <radialGradient id="sun-glow" gradientUnits="userSpaceOnUse" cx="900" cy="320" r="150">
        <stop offset="0" stop-color="#fff6c4"/>
        <stop offset="0.35" stop-color="#f7d56a" stop-opacity="0.75"/>
        <stop offset="1" stop-color="#f0b24a" stop-opacity="0"/>
      </radialGradient>
    </defs>
    <rect class="sky" x="0" y="0" width="1200" height="480" fill="url(#sky)"/>
    <rect class="spine-band" x="568" y="0" width="62" height="460" fill="#ffffff" fill-opacity="0.07"/>
    <circle class="silhouette-area" role="img"
          aria-label="Silhouette of a man sitting beside his dog on a hilltop against the setting sun"
          cx="900" cy="320" r="150" fill="url(#sun-glow)"/>
    <path class="hill" fill="#000000"
          d="M0,470 C80,455 150,436 240,432 C340,428 420,438 520,446 C600,452 660,448 730,438 C800,430 900,424 1000,425 C1100,426 1160,440 1200,445 L1200,885 L0,885 Z"/>
  </svg>

  <h2 class="back-title"><span class="line-one">GRANDPA'S</span><span class="line-two">OLD MULE</span></h2>
  <p class="back-blurb">Lorem Ipsum is simply dummy text of the printing and typesetting industry. Lorem Ipsum has been the industry's standard dummy text ever since the 1500s, when an unknown printer took a galley of type and scrambled it to make a type specimen book. It has survived not only five centuries, but also the leap into electronic typesetting, remaining essentially unchanged. It was popularised in the 1960s with the release of Pressfleet sheets containing Lorem Ipsum passages, and more recently with desktop publishing software like Quillpage Composer including versions of Lorem Ipsum.</p>

  <div class="author-photo" role="img" aria-label="Author portrait"></div>
  <p class="back-bio">Lorem Ipsum is simply dummy text of the printing and typesetting industry. Lorem Ipsum has been the industry's standard dummy text ever since the 1500s, when an unknown printer took a galley of type and scrambled it to make a type specimen book. It has survived not only five centuries, but also the leap into electronic typesetting, remaining essentially unchanged. It was popularised in the 1960s with the release of Pressfleet sheets containing Lorem Ipsum passages, and more recently with desktop publishing software like Quillpage Composer including versions of Lorem Ipsum.</p>

  <div class="spine-title">GRANDPA'S OLD MULE</div>
  <div class="spine-author">ROB T. VENSTER</div>

  <div class="front-author">ROB T. VENSTER</div>
  <h1 class="front-title">
    <span class="word-grandpa">GRANDPA'S</span>
    <span class="word-old">OLD</span>
    <span class="word-mule">MULE</span>
  </h1>
</main>
</body>
</html>
```